Business card design for a Cloud Service Provider Company

We already have business card and would like to update and get a different design. Our company is Managed IT services and Cloud Solutions Company, Tevro Systems. Attached is our current logo, current business card and sample design. I am not sure if we still need to keep our partners details on the back of the card as it does not look good to me... Please let me know if you need any additional information...

Target Market(s)

Any verticals with IT infrastructure - CEOs, CFOs and CIOs

Industry/Entity Type

Information Technology

Requirements
Must have
• First Name Last Name
• Phone
• Email address
• Company Logo

```html
<!DOCTYPE html>
<html lang="en">
<head>
<meta charset="utf-8">
<title>Tevro Systems – Business Card</title>
<link rel="stylesheet" href="https://fonts.googleapis.com/css2?family=Arimo:wght@400;700&display=swap">
<style>
  :root {
    --backdrop: #2a2a2a;
    --card-white: #f7f7f7;
    --ink: #2d2d2d;
    --brand-blue: #1a95c8;
    --brand-green: #86c231;
    --on-blue: #ffffff;
  }
  * { box-sizing: border-box; margin: 0; padding: 0; }
  html, body {
    width: 1200px; height: 997px; overflow: hidden;
    background: var(--backdrop);
    font-family: "Arimo", Arial, sans-serif;
  }
  .canvas {
    position: relative; width: 1200px; height: 997px;
  }
  .card {
    position: absolute; top: 355px;
    width: 500px; height: 286px;
    background: var(--card-white);
    border-radius: 18px;
    overflow: hidden;
    box-shadow: 0 12px 30px rgba(0,0,0,0.45);
  }
  .card--contact { left: 70px; }
  .card--front { left: 630px; }
  .card__swoosh { position: absolute; inset: 0; width: 100%; height: 100%; }

  .wordmark {
    position: absolute;
    font-weight: 700;
    color: var(--ink);
    letter-spacing: -1px;
    line-height: 1;
  }
  .card--contact .wordmark { top: 26px; right: 34px; font-size: 40px; }
  .card--front .wordmark { top: 92px; left: 0; right: 0; text-align: center; font-size: 78px; }

  .holder {
    position: absolute; left: 28px; top: 104px;
  }
  .holder__name {
    font-size: 17px; font-weight: 400; color: var(--brand-blue);
    letter-spacing: 0.5px; text-transform: uppercase; line-height: 1.2;
  }
  .holder__title {
    font-size: 11px; color: var(--ink); margin-top: 2px; line-height: 1.2;
  }

  .contacts {
    position: absolute; left: 28px; bottom: 20px;
    list-style: none;
  }
  .contacts__item {
    display: flex; align-items: center; gap: 9px;
    color: var(--on-blue); font-size: 12px; letter-spacing: 0.4px;
    margin-top: 7px; line-height: 14px;
  }
  .contacts__icon { width: 14px; height: 14px; flex: none; }

  .site {
    position: absolute; right: 24px; bottom: 34px;
    color: var(--on-blue); font-size: 12px; letter-spacing: 4px;
  }
</style>
</head>
<body>
<main class="canvas">

  <section class="card card--contact" aria-label="Business card, contact side">
    <svg class="card__swoosh" viewBox="0 0 500 286" preserveAspectRatio="none" aria-hidden="true">
      <path d="M0,168 C150,150 330,100 500,76 L500,88 C330,112 150,162 0,176 Z" fill="var(--brand-green)"/>
      <path d="M0,182 C150,168 330,118 500,94 L500,286 L0,286 Z" fill="var(--brand-blue)"/>
    </svg>
    <div class="wordmark">tevro</div>
    <div class="holder">
      <p class="holder__name">Lena Hardwick</p>
      <p class="holder__title">President</p>
    </div>
    <ul class="contacts">
      <li class="contacts__item">
        <svg class="contacts__icon" viewBox="0 0 14 14" aria-hidden="true"><circle cx="7" cy="7" r="7" fill="var(--on-blue)"/><rect x="5" y="3.5" width="4" height="7" rx="1" fill="var(--brand-blue)"/></svg>
        555-XXX-XXXX
      </li>
      <li class="contacts__item">
        <svg class="contacts__icon" viewBox="0 0 14 14" aria-hidden="true"><circle cx="7" cy="7" r="7" fill="var(--on-blue)"/><path d="M4,5 Q4,4 5,4 L6,4 L6.5,6 L5.5,6.7 Q6.5,8.5 7.5,8.7 L8,8 L10,8.5 L10,9.5 Q10,10.3 9,10.3 Q4,10 4,5 Z" fill="var(--brand-blue)"/></svg>
        555-014-2276
      </li>
      <li class="contacts__item">
        <svg class="contacts__icon" viewBox="0 0 14 14" aria-hidden="true"><circle cx="7" cy="7" r="7" fill="var(--on-blue)"/><rect x="3.5" y="4.5" width="7" height="5" fill="none" stroke="var(--brand-blue)" stroke-width="1"/><path d="M3.5,4.5 L7,7.5 L10.5,4.5" fill="none" stroke="var(--brand-blue)" stroke-width="1"/></svg>
        lhardwick@tevro.com
      </li>
    </ul>
  </section>

  <section class="card card--front" aria-label="Business card, logo side">
    <svg class="card__swoosh" viewBox="0 0 500 286" preserveAspectRatio="none" aria-hidden="true">
      <path d="M170,286 C250,230 370,195 500,178 L500,188 C370,205 260,240 190,286 Z" fill="var(--brand-green)"/>
      <path d="M215,286 C290,245 390,210 500,196 L500,286 Z" fill="var(--brand-blue)"/>
    </svg>
    <div class="wordmark">tevro</div>
    <p class="site">www.tevro.com</p>
  </section>

</main>
</body>
</html>
```